Italian restaurant needs a flyer to promote wine tasting and wine pairing tours

Need a designer to create one flyer for print and digital use.

(3 pages all either postcard or 1/3 page)Intro page, wine tasting and wine pairing page, wine pairing and cruise page

We are Www.corvalutrattoria.com an top rated Italian restaurant in CABO San Lucas mexico. Our info and history is on the website. We are a fun, cozy bistro ambience that makes you feel like you are in Italy.

Get to know the great tastes of Rome right here in CABO San Lucas at Corvalu Bistro. Farm and sea to table and select national and international wines . We begin with a brief introduction of the restaurant including a quick Salute to the kitchen then sit at our reserved table for a fun and tasty wine food pairing.

Our Founding Chef and In House Sommelier join forces to create four fabulous farm and sea to table dishes, using the freshest ingredients from local sources and only the top wines from small vineyards. Guests are guided through four wine & food pairings, with a some fun facts about wine and the wine producing regions of Mexico. A lively resort casual setting and a night you will never forget.

Wine & Dine Pairing Session includes:
* Welcome cocktail!
* 4-Course Wine Pairing menu
* Each course paired with local wines
* After Tasting Night cap
* Regional history, Wine tasting tips, trivia, and prizes!
* Guests receive 20% off their next reservation
* Everyday at 5:30pm and 9:30pm for one hour and 45 minutes.
* Limited to 10 guests per session please reserve in advance.
* 69usd X person. Tax included .

Target Market(s)

Wine lovers coming to CABO San Lucas

Industry/Entity Type

Restaurant

Font styles to use
Serif

Requirements
Must have
• More image and less text with an elegant yet fun setting
• Must have wine and dine description:
• Get to know the great tastes of Rome right here in CABO San Lucas at Corvalu Bistro. Farm and sea to table and select national and international wines . We begin with a brief introduction of the restaurant including a quick Salute to the kitchen then sit at our reserved table for a fun and tasty wine food pairing.
• Our Founding Chef and In House Sommelier join forces to create four fabulous farm and sea to table dishes, using the freshest ingredients from local sources and only the top wines from small vineyards. Guests are guided through four wine & food pairings, with a some fun facts about wine and the wine producing regions of Mexico. A lively resort casual setting and a night you will never forget.
• Wine & Dine Pairing Session includes:
• * Welcome cocktail!
• * 4-Course Wine Pairing menu
• * Each course paired with local wines
• * After Tasting Night cap
• * Regional history, Wine tasting tips, trivia, and prizes!
• * Guests receive 20% off their next reservation
• * Everyday at 5:30pm and 9:30pm for one hour and 45 minutes.
• * Limited to 10 guests per session please reserve in advance.
• * 69usd X person. Tax included .
• amd must have wine tasting description:
• One hour of fun and flavor!
• Join our in house sommelier in this small group, one hour , lively happy hour party that includes ample tastes of 3 fine wines paired with authentic Italian gourmet appetizers and seasonal menu favorites. Let us share the best of Bajas wines amd perfectly paired tasting menu before hitting the town.
• This Wine Tasting Happy hour includes:
• * Welcome cocktail!
• * 4-Course Tasting menu
• * Each course paired with Baja local wines
• * Starts at 5pm or 6pm. Arrive 5 minutes prior for check in. Space is limited to 20 guests so advanced reservations are recommended.
• * 25usd per person tax included.
• Colors should be like our website www.corvalutrattoria.com
• Files must be editable
Nice to have
• Want this to focus on promoting the restaurant and tours
Should not have
• Errors

```html
<!DOCTYPE html>
<html lang="en">
<head>
<meta charset="utf-8">
<title>Corvalu Bistro – Wine Tasting Flyer</title>
<link href="https://fonts.googleapis.com/css2?family=Cinzel:wght@400;600&family=Lato:wght@400;700&family=Montserrat:wght@800&display=swap" rel="stylesheet">
<style>
  :root {
    --page-bg: #2e2a27;
    --card-bg: #1a1a1a;
    --accent: #e8901e;
    --gold: #d9a63a;
    --text: #ececec;
    --white: #ffffff;
    --photo-deep: #140c08;
  }
  * { box-sizing: border-box; margin: 0; padding: 0; }
  html, body {
    width: 1200px; height: 1200px; overflow: hidden;
    background: var(--page-bg);
    font-family: "Lato", sans-serif;
    color: var(--text);
  }
  .card {
    position: absolute; left: 69px; width: 1046px; height: 509px;
    background: var(--card-bg); overflow: hidden;
  }
  .card--intro { top: 58px; }
  .card--details { top: 613px; }

  .photo {
    position: absolute; top: 0; bottom: 0; right: 0;
    background:
      radial-gradient(ellipse at 35% 75%, rgba(138,74,30,.55), transparent 55%),
      radial-gradient(ellipse at 80% 30%, rgba(90,42,20,.6), transparent 60%),
      linear-gradient(90deg, var(--card-bg) 0%, var(--photo-deep) 25%, #24140c 100%);
  }
  .card--intro .photo { left: 560px; }
  .card--details .photo { left: 840px; }

  .brand {
    position: absolute; display: flex; align-items: center; gap: 10px;
    font-family: "Cinzel", serif; font-weight: 400; color: var(--gold);
    letter-spacing: .05em; line-height: 1.15; text-align: center;
  }
  .brand__dot { border-radius: 50%; background: var(--gold); flex: none; }
  .card--intro .brand { left: 56px; top: 62px; width: 200px; font-size: 30px; }
  .card--intro .brand__dot { width: 14px; height: 14px; }
  .card--details .brand { left: 96px; top: 26px; width: 120px; font-size: 17px; }
  .card--details .brand__dot { width: 9px; height: 9px; }

  .title { position: absolute; left: 285px; top: 56px; font-weight: normal; }
  .title__top {
    font-family: "Montserrat", sans-serif; font-weight: 800;
    font-size: 43px; line-height: 1; color: var(--white); letter-spacing: .01em;
  }
  .title__main {
    font-family: "Cinzel", serif; font-weight: 400;
    font-size: 62px; line-height: 1; margin-top: 6px; color: var(--accent);
  }

  .intro-copy {
    position: absolute; left: 30px; top: 230px; width: 424px;
    font-size: 14.6px; line-height: 18.6px; text-align: justify;
  }
  .intro-copy p + p { margin-top: 20px; }

  .section-head {
    color: var(--accent); font-weight: 700; font-size: 19px;
    padding-bottom: 4px; border-bottom: 2px solid var(--text);
    display: inline-block;
  }
  .col-left { position: absolute; left: 34px; top: 106px; width: 300px; }
  .col-right { position: absolute; left: 371px; top: 40px; width: 448px; }

  .tagline {
    font-family: "Cinzel", serif; font-weight: 400; color: var(--accent);
    font-size: 29px; line-height: 1.2; padding-bottom: 3px;
    border-bottom: 2px solid var(--text); display: inline-block;
  }
  .tasting-copy {
    margin-top: 22px; font-size: 14.6px; line-height: 18.6px; width: 443px;
  }
  .col-right .section-head { margin-top: 14px; }

  .perks { list-style: none; margin-top: 17px; }
  .perks li {
    position: relative; padding-left: 30px;
    font-size: 15px; line-height: 19px;
  }
  .perks li::before {
    content: ""; position: absolute; left: 10px; top: 6px;
    width: 8px; height: 8px; border-radius: 50%; background: var(--accent);
  }
  .col-left .perks li + li { margin-top: 12px; }
  .col-right .perks { margin-top: 12px; width: 340px; }
  .col-right .perks li + li { margin-top: 8.5px; }
</style>
</head>
<body>

<section class="card card--intro">
  <div class="photo" role="img" aria-label="Photo of a glass wine decanter, wine glasses and a row of red wine bottles in warm low light"></div>
  <div class="brand"><span class="brand__dot"></span><span>Corvalu<br>Bistro</span></div>
  <h1 class="title">
    <div class="title__top">WELCOME</div>
    <div class="title__main">COCKTAIL!</div>
  </h1>
  <div class="intro-copy">
    <p>Get to know the great tastes of Rome right here in CABO San Lucas at Corvalu Bistro. Farm and sea to table and select national and international wines. We begin with a brief introduction of the restaurant including a quick Salute to the kitchen then sit at our reserved table for a fun and tasty wine food pairing.</p>
    <p>Our Founding Chef and In House Sommelier join forces to create four fabulous farm and sea to table dishes, using the freshest ingredients from local sources and only the top wines from small vineyards. Guests are guided through four wine &amp; food pairings, with some fun facts about wine and the wine producing regions of Mexico. A lively resort casual setting and a night you will never forget.</p>
  </div>
</section>

<section class="card card--details">
  <div class="photo" role="img" aria-label="Photo of a glass wine decanter with wine glasses and bottles behind it"></div>
  <div class="brand"><span class="brand__dot"></span><span>Corvalu<br>Bistro</span></div>

  <div class="col-left">
    <h2 class="section-head">Wine &amp; Dine Pairing Session</h2>
    <ul class="perks">
      <li>Welcome cocktail!</li>
      <li>4-Course Wine Pairing menu</li>
      <li>Each course paired with local wines</li>
      <li>After Tasting Night cap</li>
      <li>Regional history, Wine tasting tips, trivia, and prizes!</li>
      <li>Guests receive 20% off their next reservation</li>
      <li>Everyday at 5:30pm and 9:30pm for one hour and 45 minutes.</li>
      <li>Limited to 10 guests per session please reserve in advance.</li>
      <li>69usd X person. Tax included</li>
    </ul>
  </div>

  <div class="col-right">
    <h2 class="tagline">One hour of fun &amp; flavor!</h2>
    <p class="tasting-copy">Join our in house sommelier in this small group, one hour, lively happy hour party that includes ample tastes of 3 fine wines paired with authentic Italian gourmet appetizers and seasonal menu favorites. Let us share the best of Baja's wines and perfectly paired tasting menu before hitting the town.</p>
    <h3 class="section-head">This Wine Tasting Happy hour</h3>
    <ul class="perks">
      <li>Welcome cocktail!</li>
      <li>4-Course Tasting menu</li>
      <li>Each course paired with Baja local wines</li>
      <li>Regional history, Wine tasting tips, trivia, and prizes!</li>
      <li>Guests receive 20% off their next reservation</li>
      <li>Starts at 5pm or 6pm. Arrive 5 minutes prior for check in. Space is limited to 20 guests so advanced reservations are recommended.</li>
      <li>25usd per person tax included.</li>
    </ul>
  </div>
</section>

</body>
</html>
```